Korvane Sky Works, LLC - Business Card

I currently have a drone business that specializes in aerial photography, thermal image inspections, deer recovery, search and rescue, custom agricultural applications. i will attach my current business card as well as some logos to incorporate for a new up to date business card
Updates

Designs look the same

Sick

Target Market(s)

farmers, hunters

Contact Information for Business Card

name address phone number (as existing card i attached)

Requirements
Must have
• im good with existing business card, but would like an agricultural twist

```html
<!DOCTYPE html>
<html lang="en">
<head>
<meta charset="utf-8">
<title>Korvane Sky Works, LLC – Business Card</title>
<link href="https://fonts.googleapis.com/css2?family=Roboto:wght@400;500;900&display=swap" rel="stylesheet">
<style>
  :root {
    --backdrop: #2b2b2b;
    --paper: #f7f7f5;
    --green: #3f9a1e;
    --green-deep: #2c7a12;
    --green-light: #5cb52f;
    --grey: #8a8a8a;
    --grey-dark: #4a4a4a;
    --ink: #555555;
    --social: #2f67c4;
    --white: #ffffff;
  }
  * { box-sizing: border-box; margin: 0; padding: 0; }
  html, body {
    width: 1200px; height: 852px; overflow: hidden;
    background: var(--backdrop);
    font-family: "Roboto", Arial, sans-serif;
  }
  .card {
    position: absolute;
    width: 525px; height: 300px;
    background: var(--paper);
    border-radius: 18px;
    overflow: hidden;
  }
  .card--front { left: 80px; top: 90px; }
  .card--back { left: 595px; top: 462px; }

  .brand {
    display: flex; align-items: center; gap: 10px;
    color: var(--green);
    font-weight: 900;
    letter-spacing: 1px;
  }
  .brand__dot {
    width: 22px; height: 22px; border-radius: 50%;
    background: var(--green);
  }
  .card--front .brand {
    position: absolute; left: 50%; top: 50%;
    transform: translate(-50%, -50%);
    font-size: 44px;
  }
  .card--back .brand {
    position: absolute; right: 44px; top: 30px;
    font-size: 30px;
  }
  .card--back .brand__dot { width: 16px; height: 16px; }

  .wave { position: absolute; left: 0; top: 0; width: 525px; height: 300px; }

  .identity { position: absolute; left: 40px; top: 70px; }
  .identity__name {
    font-size: 25px; font-weight: 900; color: var(--green); line-height: 30px;
  }
  .identity__role {
    margin-top: 4px; font-size: 12px; color: var(--ink);
  }
  .identity__social {
    margin-top: 16px; display: flex; align-items: center; gap: 7px;
    font-size: 12px; color: var(--ink);
  }
  .identity__social-dot {
    width: 13px; height: 13px; border-radius: 50%; background: var(--social);
  }

  .contact {
    position: absolute; left: 40px; top: 224px;
    list-style: none; color: var(--white); font-size: 12.5px;
  }
  .contact li {
    display: flex; align-items: center; gap: 9px; height: 17px;
  }
  .contact svg { width: 12px; height: 12px; fill: var(--white); flex: none; }
</style>
</head>
<body>

<section class="card card--front" aria-label="Card front">
  <div class="brand"><span class="brand__dot"></span>Korvane</div>
</section>

<section class="card card--back" aria-label="Card back">
  <svg class="wave" viewBox="0 0 525 300" preserveAspectRatio="none" aria-hidden="true">
    <defs>
      <linearGradient id="fieldGreen" x1="0" y1="1" x2="1" y2="0">
        <stop offset="0" stop-color="#2c7a12"/>
        <stop offset="0.5" stop-color="#45a01f"/>
        <stop offset="1" stop-color="#2f8015"/>
      </linearGradient>
    </defs>
    <path d="M0 192 C120 168 250 162 360 142 C440 128 495 98 525 66 L525 300 L0 300 Z" fill="var(--grey)"/>
    <path d="M0 200 C120 176 250 170 360 150 C440 136 495 108 525 78 L525 300 L0 300 Z" fill="var(--paper)"/>
    <path d="M0 204 C120 180 250 174 360 155 C440 142 495 116 525 88 L525 300 L0 300 Z" fill="var(--grey-dark)"/>
    <path d="M0 214 C120 192 250 186 360 168 C440 156 495 132 525 104 L525 300 L0 300 Z" fill="url(#fieldGreen)"/>
  </svg>

  <div class="brand"><span class="brand__dot"></span>Korvane</div>

  <div class="identity">
    <h1 class="identity__name">Dalton Reese</h1>
    <p class="identity__role">Owner</p>
    <p class="identity__social"><span class="identity__social-dot"></span>Korvane-Sky-Works</p>
  </div>

  <ul class="contact">
    <li>
      <svg viewBox="0 0 12 12"><path d="M2.5 0.5 L4.5 0.5 L5.2 3.2 L3.8 4.3 C4.5 5.8 6 7.3 7.6 8.1 L8.8 6.8 L11.5 7.5 L11.5 9.5 C11.5 10.6 10.6 11.5 9.5 11.5 C4.8 11.2 0.8 7.2 0.5 2.5 C0.5 1.4 1.4 0.5 2.5 0.5 Z"/></svg>
      555-014-2290
    </li>
    <li>
      <svg viewBox="0 0 12 12"><circle cx="6" cy="6" r="5.3" fill="none" stroke="#fff" stroke-width="1.1"/><ellipse cx="6" cy="6" rx="2.3" ry="5.3" fill="none" stroke="#fff" stroke-width="1"/><path d="M0.8 6 H11.2" stroke="#fff" stroke-width="1"/></svg>
      www.korvaneskyworks.com
    </li>
    <li>
      <svg viewBox="0 0 12 12"><rect x="0.5" y="2" width="11" height="8" rx="1"/><path d="M0.8 2.4 L6 6.6 L11.2 2.4" fill="none" stroke="#3f9a1e" stroke-width="1"/></svg>
      hello@korvaneskyworks.com
    </li>
    <li>
      <svg viewBox="0 0 12 12"><path d="M6 0.5 C3.6 0.5 2 2.3 2 4.4 C2 7.2 6 11.5 6 11.5 C6 11.5 10 7.2 10 4.4 C10 2.3 8.4 0.5 6 0.5 Z"/><circle cx="6" cy="4.4" r="1.4" fill="#3f9a1e"/></svg>
      214 W. Elm St. Marlow, OH 45000
    </li>
  </ul>
</section>

</body>
</html>
```